The most modern business card ever !!!

Our company call “Tavlin”. Tavlin is a technology company specialized in cruises solutions. Out main product is a platform to reserve cruises. This is a revolutionary platform that make easier to travel agencies and final users to reserve cruises across dozen companies like brindle, pelvo, tkw, vbd, etc..We are a “start up”, with a young team of developers and we want to transmit it.. For it, we want something different, a modern business card that represent cruises and technology.. When someone receive this card, this person should say: wowww this is different… this is modern… this is a cruise related company..
Contact Information for Business Card
Requirements
Must have
- diferent, modern
Should not have
- traditions business card

```html
<!DOCTYPE html>
<html lang="en">
<head>
<meta charset="utf-8">
<title>Tavlin Business Card</title>
<link href="https://fonts.googleapis.com/css2?family=Exo+2:wght@600&family=Roboto:wght@400;500&display=swap" rel="stylesheet">
<style>
  :root {
    --page: #ffffff;
    --card: #1c1c1c;
    --accent: #27a3dc;
    --ink: #ffffff;
    --ghost: #242424;
    --logo: #c4c4c4;
  }
  html, body {
    margin: 0;
    width: 1200px;
    height: 1200px;
    overflow: hidden;
    background: var(--page);
  }
  .canvas { position: relative; width: 1200px; height: 1200px; }
  .card {
    position: absolute;
    top: 181px;
    width: 480px;
    height: 840px;
    background: var(--card);
    overflow: hidden;
    font-family: "Roboto", Arial, sans-serif;
    color: var(--ink);
  }
  .card--front { left: 111px; }
  .card--back { left: 612px; }
  .ghost-name {
    position: absolute;
    top: 30px;
    left: 0;
    width: 100%;
    text-align: center;
    font-family: "Roboto", Arial, sans-serif;
    font-weight: 500;
    font-size: 104px;
    line-height: 1;
    color: var(--ghost);
    letter-spacing: 4px;
  }
  .centered {
    position: absolute;
    left: 0;
    width: 100%;
    text-align: center;
  }
  .person-name {
    top: 262px;
    font-family: "Exo 2", Arial, sans-serif;
    font-weight: 600;
    font-size: 44px;
    line-height: 56px;
    color: var(--accent);
    letter-spacing: 1px;
  }
  .person-role {
    top: 316px;
    font-size: 18px;
    line-height: 24px;
    letter-spacing: 0.5px;
  }
  .rule {
    position: absolute;
    height: 2px;
    background: var(--accent);
  }
  .rule--title { top: 348px; left: 157px; width: 166px; }
  .rule--left { top: 751px; left: 0; width: 114px; }
  .rule--right { top: 751px; left: 365px; width: 115px; }
  .contact-icon {
    position: absolute;
    left: 227px;
    width: 26px;
    height: 26px;
  }
  .contact-text {
    font-size: 20px;
    line-height: 26px;
    letter-spacing: 0.6px;
  }
  .address {
    top: 727px;
    font-size: 19px;
    line-height: 24px;
    letter-spacing: 0.5px;
  }
  .brand-name {
    position: absolute;
    left: 35px;
    top: 676px;
    font-family: "Roboto", Arial, sans-serif;
    font-weight: 500;
    font-size: 112px;
    line-height: 1;
    color: var(--logo);
    letter-spacing: 6px;
  }
</style>
</head>
<body>
<main class="canvas">
  <section class="card card--front" aria-label="Card front">
    <div class="ghost-name" aria-hidden="true">Tavlin</div>

    <h1 class="centered person-name" style="margin:0">Owen Marsh</h1>
    <div class="centered person-role">Founder &amp; CEO</div>
    <div class="rule rule--title"></div>

    <svg class="contact-icon" style="top:426px" viewBox="0 0 26 26" aria-hidden="true">
      <circle cx="13" cy="13" r="13" fill="var(--accent)"/>
      <path d="M8.5 7.5c.6-.6 1.4-.5 1.8.1l1.2 1.8c.3.5.2 1.1-.2 1.5l-.7.6c.6 1.4 1.6 2.5 3 3.2l.6-.7c.4-.4 1-.5 1.5-.2l1.8 1.2c.6.4.7 1.2.1 1.8l-.8.8c-.8.8-2 .9-3 .4-3-1.5-5.3-3.8-6.8-6.8-.5-1-.4-2.2.4-3z" fill="#1c1c1c"/>
    </svg>
    <div class="centered contact-text" style="top:459px">000 000 0000</div>

    <svg class="contact-icon" style="top:513px" viewBox="0 0 26 26" aria-hidden="true">
      <circle cx="13" cy="13" r="13" fill="var(--accent)"/>
      <rect x="6.5" y="8.5" width="13" height="9" rx="1.5" fill="#1c1c1c"/>
      <path d="M7 9.5l6 4.2 6-4.2" fill="none" stroke="var(--accent)" stroke-width="1.3"/>
    </svg>
    <div class="centered contact-text" style="top:546px">o.marsh@tavlin.com</div>

    <svg class="contact-icon" style="top:600px;left:224px" viewBox="0 0 26 26" aria-hidden="true">
      <circle cx="13" cy="13" r="13" fill="var(--accent)"/>
      <g fill="none" stroke="#1c1c1c" stroke-width="1.2">
        <circle cx="13" cy="13" r="6.5"/>
        <ellipse cx="13" cy="13" rx="3" ry="6.5"/>
        <path d="M6.5 13h13M7.5 9.8h11M7.5 16.2h11"/>
      </g>
    </svg>
    <div class="centered contact-text" style="top:633px">www.tavlin.com</div>

    <div class="rule rule--left"></div>
    <div class="centered address">48 Harbour Lane, Suite# B<br>Dover, UK 410B27</div>
    <div class="rule rule--right"></div>
  </section>

  <section class="card card--back" aria-label="Card back">
    <div class="ghost-name" aria-hidden="true">Tavlin</div>
    <div class="brand-name">Tavlin</div>
  </section>
</main>
</body>
</html>
```